Book cover design for Verses for Lantern and Harbor, 30th Anniversary Revised Edition

Simple, clean book cover design for the 30th Anniversary Edition of "Verses for Lantern and Harbor" by noted author Quentin Halloway. Mostly typographical design, but also with an integrated design icon that immediately captures and conveys the sense of "science and industry" (a gear inside a science beaker? Atoms revolving around a nucleus? Etc. This is where your creativity comes in, and will be a critical element of the final cover design).

Book cover will be printed in one color only (black/screened gray)

Book/cover trim size: 5 3/8" x 8 1/2 "

Cover elements (all of these must be present):

Title: Verses for Lantern and Harbor
Author: Quentin Halloway
Reading/tag line: 30th Anniversary Revised Edition
Design element

*
Your design will be acknowledged in the book.

I look forward to seeing your submission!
Updates

Book/cover trim size is 5 3/8" x 8 1/2"

Industry/Entity Type

Industry

Requirements
Must have
• Cover elements (all of these must be present):
• Title: Verses for Lantern and Harbor
• Author: Quentin Halloway
• Reading/tag line: 30th Anniversary Revised Edition
• Design element
Should not have
• No color -- black and grayscale only

```html
<!DOCTYPE html>
<html lang="en">
<head>
<meta charset="utf-8">
<title>Verses for Lantern and Harbor — Cover Spread</title>
<link href="https://fonts.googleapis.com/css2?family=Cinzel:wght@400;600;700&display=swap" rel="stylesheet">
<style>
  :root {
    --ink: #0d0d0d;
    --sky-top: #1e1e1e;
    --sky-mid: #3a3a3a;
    --sky-low: #5c5c5c;
    --horizon: #767676;
    --haze: #444444;
    --ground: #0b0b0b;
    --glow: rgba(220,220,220,0.35);
    --frame: #8a8a8a;
    --frame-edge: #bdbdbd;
    --title: #d9d9d9;
    --paper: #f5f5f5;
    --emblem: #cfcfcf;
  }
  * { margin: 0; padding: 0; box-sizing: border-box; }
  html, body { width: 1200px; height: 928px; overflow: hidden; background: var(--ink); }
  .spread {
    position: relative; width: 1200px; height: 928px;
    background: linear-gradient(180deg, #262626 0%, #161616 60%, #0e0e0e 100%);
    font-family: "Cinzel", "Times New Roman", serif;
  }
  .scene {
    position: absolute;
    background:
      radial-gradient(ellipse 70% 22% at 45% 78%, var(--glow), transparent 70%),
      linear-gradient(180deg, var(--sky-top) 0%, var(--sky-mid) 35%, var(--sky-low) 62%, var(--horizon) 72%, var(--haze) 80%, var(--ground) 94%);
  }
  .scene--back { left: 26px; top: 36px; width: 553px; height: 863px; }
  .scene--front { left: 623px; top: 36px; width: 556px; height: 863px; }
  .frame {
    position: absolute; border: 6px solid var(--frame);
    box-shadow: inset 0 0 0 1px var(--frame-edge), 0 0 0 1px rgba(189,189,189,0.4);
  }
  .frame--back { left: 20px; top: 30px; width: 565px; height: 875px; }
  .frame--front { left: 617px; top: 30px; width: 568px; height: 875px; }
  .title, .spine-title {
    color: var(--title);
    text-shadow: 0 1px 2px rgba(0,0,0,0.6);
    font-weight: 600; letter-spacing: 1px;
  }
  .cover-text { position: absolute; text-align: center; }
  .cover-text--front { left: 617px; width: 568px; top: 102px; }
  .cover-text--back { left: 160px; width: 356px; top: 344px; }
  .cover-text--front .title { font-size: 38px; line-height: 58px; }
  .cover-text--back .title { font-size: 25px; line-height: 42px; }
  .tagline { color: var(--paper); font-weight: 600; letter-spacing: 0.5px; }
  .cover-text--front .tagline { font-size: 18px; margin-top: 6px; }
  .cover-text--back .tagline { font-size: 13px; margin-top: 2px; }
  .author { position: absolute; color: var(--paper); font-weight: 600; letter-spacing: 1px; }
  .author--front { left: 617px; width: 568px; text-align: center; top: 852px; font-size: 22px; }
  .author--back { left: 210px; width: 260px; text-align: center; top: 490px; font-size: 20px; }
  .emblem { position: absolute; left: 846px; top: 330px; width: 110px; height: 110px; }
  .spine {
    position: absolute; left: 585px; top: 30px; width: 32px; height: 875px;
    display: flex; align-items: center; justify-content: center;
  }
  .spine-title {
    writing-mode: vertical-rl; white-space: nowrap;
    font-size: 30px; letter-spacing: 2.5px;
  }
</style>
</head>
<body>
<main class="spread">
  <div class="scene scene--back" role="img" aria-label="Photograph of an illuminated industrial refinery with a tall stack under a dusk sky, in grayscale"></div>
  <div class="scene scene--front" role="img" aria-label="Photograph of refinery towers lit with lamps against an evening sky, in grayscale"></div>

  <div class="frame frame--back"></div>
  <div class="frame frame--front"></div>

  <section class="cover-text cover-text--back">
    <h2 class="title">VERSES FOR<br>LANTERN AND HARBOR</h2>
    <p class="tagline">30TH ANNIVERSARY REVISED EDITION</p>
  </section>
  <p class="author author--back">QUENTIN HALLOWAY</p>

  <div class="spine"><span class="spine-title">VERSES FOR LANTERN AND HARBOR</span></div>

  <section class="cover-text cover-text--front">
    <h1 class="title">VERSES FOR<br>LANTERN AND HARBOR</h1>
    <p class="tagline">30TH ANNIVERSARY REVISED EDITION</p>
  </section>

  <svg class="emblem" viewBox="0 0 110 110" role="img" aria-label="Atom emblem for science and industry">
    <g fill="none" stroke="var(--emblem)" stroke-width="2.5">
      <ellipse cx="55" cy="55" rx="48" ry="17"/>
      <ellipse cx="55" cy="55" rx="48" ry="17" transform="rotate(60 55 55)"/>
      <ellipse cx="55" cy="55" rx="48" ry="17" transform="rotate(-60 55 55)"/>
    </g>
    <circle cx="55" cy="55" r="7" fill="var(--emblem)"/>
  </svg>

  <p class="author author--front">QUENTIN HALLOWAY</p>
</main>
</body>
</html>
```